Willow Brook Meadows - Pelham Ridge Loop

Please use this range of Flyers. Info can be found on our Facebook Page Willow Brook Meadows. W

Colour range- Black with Orange Trim. Logo attached.

Target Market(s)

Horse Owners

Colors
ffcf3e
f78f20
f37122

Requirements
Must have
• Our Logo. Tri-fold
Should not have
• Other photos other than supplied. Do not mix Willow Brook Meadows with Willow Brook Equine Sanctuary. This is only for Willow Brook Meadows.

```html
<!DOCTYPE html>
<html lang="en">
<head>
<meta charset="utf-8">
<title>Willow Brook Meadows – Tri-fold Brochure</title>
<link rel="stylesheet" href="https://fonts.googleapis.com/css2?family=Cinzel:wght@400;600&family=Poppins:wght@400;500;700&display=swap">
<style>
  :root {
    --page-bg: #d3d3d3;
    --paper: #ffffff;
    --ink: #4a4a4a;
    --ink-dark: #3d3d3d;
    --red: #e3462f;
    --orange: #f37122;
    --orange-light: #f78f20;
    --black: #1b1b1b;
    --white: #ffffff;
  }
  * { margin: 0; padding: 0; box-sizing: border-box; }
  html, body { width: 1200px; height: 1161px; overflow: hidden; background: var(--page-bg); }
  .brochure {
    position: absolute; left: 30px; top: 178px;
    width: 1140px; height: 806px;
    background: var(--paper);
    overflow: hidden;
  }
  .brochure__art { position: absolute; inset: 0; width: 1140px; height: 806px; }
  .panel { position: absolute; top: 0; width: 380px; height: 806px; }
  .panel--about { left: 0; }
  .panel--contact { left: 380px; }
  .panel--cover { left: 760px; }

  .about__title {
    position: absolute; top: 280px; left: 0; width: 380px; text-align: center;
    font-family: "Cinzel", serif; font-weight: 600; font-size: 27px; color: var(--red);
  }
  .about__text {
    position: absolute; top: 322px; left: 45px; width: 290px; text-align: center;
    font-family: "Poppins", sans-serif; font-size: 14.5px; line-height: 23.3px; color: var(--ink);
  }

  .contact__title {
    position: absolute; top: 24px; left: 0; width: 380px; text-align: center;
    font-family: "Poppins", sans-serif; font-weight: 700; font-size: 23px; line-height: 1; color: var(--white);
  }
  .contact__subtitle {
    position: absolute; top: 50px; left: 0; width: 380px; text-align: center;
    font-family: "Poppins", sans-serif; font-size: 14px; color: var(--white); letter-spacing: .3px;
  }
  .contact__phone {
    position: absolute; top: 90px; left: 27px; width: 325px; height: 40px;
    background: var(--white); border-radius: 20px;
    display: flex; align-items: center; justify-content: center; gap: 12px;
    font-family: "Cinzel", serif; font-size: 29px; color: var(--red);
  }
  .contact__phone svg { width: 22px; height: 22px; }
  .contact__line {
    position: absolute; left: 0; width: 380px; text-align: center;
    font-family: "Poppins", sans-serif; font-size: 14px; color: var(--white);
  }
  .contact__line b { font-weight: 700; }
  .contact__rule { position: absolute; left: 31px; width: 312px; height: 1px; background: rgba(255,255,255,.6); }

  .wordmark {
    position: absolute; display: flex; align-items: center; gap: 12px;
    font-family: "Cinzel", serif; font-weight: 400; text-align: right; line-height: 1.02;
  }
  .wordmark__square { flex: none; }
  .wordmark--light { top: 36px; right: 58px; font-size: 30px; color: var(--white); }
  .wordmark--light .wordmark__square { width: 62px; height: 104px; background: var(--white); }
  .wordmark--accent { top: 500px; left: 50px; font-size: 31px; color: var(--orange); }
  .wordmark--accent .wordmark__square { width: 62px; height: 112px; background: var(--orange); }

  .cover__title {
    position: absolute; top: 570px; left: 0; width: 380px; text-align: center;
    font-family: "Cinzel", serif; font-weight: 600; font-size: 42px; line-height: 48px;
  }
  .cover__title-top { color: var(--ink-dark); }
  .cover__title-accent { color: var(--orange); }
  .cover__tagline {
    position: absolute; top: 722px; left: 0; width: 380px; text-align: center;
    font-family: "Poppins", sans-serif; font-size: 13.5px; color: var(--ink-dark); letter-spacing: .3px;
  }
</style>
</head>
<body>
<main class="brochure">
  <svg class="brochure__art" viewBox="0 0 1140 806">
    <defs>
      <linearGradient id="greyPhoto" x1="0" y1="0" x2="0" y2="1">
        <stop offset="0" stop-color="#f3f3f3"/>
        <stop offset="1" stop-color="#c4c4c4"/>
      </linearGradient>
      <linearGradient id="fieldPhoto" x1="0" y1="0" x2="0" y2="1">
        <stop offset="0" stop-color="#8a8478"/>
        <stop offset=".5" stop-color="#c9b89c"/>
        <stop offset="1" stop-color="#5d8a3c"/>
      </linearGradient>
      <linearGradient id="wagonPhoto" x1="0" y1="0" x2="1" y2="1">
        <stop offset="0" stop-color="#d9d9d9"/>
        <stop offset=".5" stop-color="#a8574a"/>
        <stop offset="1" stop-color="#8e8e8e"/>
      </linearGradient>
      <linearGradient id="riderPhoto" x1="0" y1="0" x2="0" y2="1">
        <stop offset="0" stop-color="#1b1b1b"/>
        <stop offset=".25" stop-color="#4e4a3e"/>
        <stop offset=".6" stop-color="#8a6a55"/>
        <stop offset="1" stop-color="#6f7d4a"/>
      </linearGradient>
    </defs>

    <rect x="380" y="330" width="380" height="476" fill="url(#greyPhoto)" role="img" aria-label="Faded photo of a carer leading a white horse over a wooden platform"/>

    <rect x="0" y="0" width="334" height="252" fill="url(#wagonPhoto)" role="img" aria-label="Photo of a grey horse beside a red wooden wagon with its handler"/>

    <path d="M0,570 C140,500 390,490 520,806" fill="none" stroke="var(--orange)" stroke-width="14"/>
    <path d="M0,588 C150,520 390,515 510,806 L0,806 Z" fill="url(#fieldPhoto)" role="img" aria-label="Photo of a saddled buckskin horse being led across a wooden walkway on grass"/>

    <path d="M380,372 C420,336 470,318 540,330 C620,344 690,400 760,448" fill="none" stroke="var(--orange)" stroke-width="10"/>
    <path d="M380,358 C420,322 470,306 540,316 C620,330 690,382 760,432 L760,0 L380,0 Z" fill="var(--red)"/>

    <path d="M760,452 C840,540 960,560 1140,428" fill="none" stroke="var(--orange)" stroke-width="14"/>
    <rect x="760" y="0" width="380" height="120" fill="var(--black)"/>
    <path d="M760,0 H1140 V408 C960,532 840,520 760,432 Z" fill="url(#riderPhoto)" role="img" aria-label="Photo of a rider in a helmet on a roan horse in a paddock"/>
  </svg>

  <section class="panel panel--about">
    <h2 class="about__title">About Us</h2>
    <p class="about__text">Our amazing property Willow Brook Meadows is a multi-faceted equine destination which includes spacious paddocks, a training arena and rehabilitation care. Our intensive rescue experience has honed an experienced team of rehabilitation carers.</p>
  </section>

  <section class="panel panel--contact">
    <h2 class="contact__title">CONTACT US</h2>
    <p class="contact__subtitle">FOR MORE INFORMATION</p>
    <div class="contact__phone">
      <svg viewBox="0 0 24 24" aria-hidden="true"><path fill="var(--red)" d="M6.6 10.8a15.1 15.1 0 0 0 6.6 6.6l2.2-2.2c.3-.3.7-.4 1-.2 1.1.4 2.3.6 3.6.6.6 0 1 .4 1 1V20c0 .6-.4 1-1 1A17 17 0 0 1 3 4c0-.6.4-1 1-1h3.5c.6 0 1 .4 1 1 0 1.3.2 2.5.6 3.6.1.3 0 .7-.2 1z"/></svg>
      <span>61 400 555 019</span>
    </div>
    <p class="contact__line" style="top:158px">info@<b>willowbrookvet</b>.com</p>
    <div class="contact__rule" style="top:196px"></div>
    <p class="contact__line" style="top:209px">www.<b>willowbrook</b>.org.au</p>
    <div class="contact__rule" style="top:247px"></div>
    <p class="contact__line" style="top:260px; line-height:21px">48 Fenwick Lane Pelham, VIC,<br>Australia 3390</p>
    <div class="wordmark wordmark--accent">
      <span>Willow<br>Brook<br>Meadows</span>
      <span class="wordmark__square"></span>
    </div>
  </section>

  <section class="panel panel--cover">
    <div class="wordmark wordmark--light">
      <span>Willow<br>Brook<br>Meadows</span>
      <span class="wordmark__square"></span>
    </div>
    <h1 class="cover__title">
      <span class="cover__title-top">Willow</span><br>
      <span class="cover__title-accent">Brook<br>Meadows</span>
    </h1>
    <p class="cover__tagline">A MULTI-FACETED EQUINE DESTINATION</p>
  </section>
</main>
</body>
</html>
```